Graphic designs required for HR consulting Website

We need to items designed to be used on our website and in presentations.
Please view our website for design ideas.
http://www.brightpeak.com.au.17.morvane.pw
See attached Powerpoint doc for more info.
InfoGraphic 1
Needs to be turned into an infographic that will be embedded into the BrightPeak HR website.
The fonts should be Helvetica Neue and should have the look and feel of the website.
InfoGraphic 2
Needs to be turned into an infographic that will be embedded into the BrightPeak HR website and used in PPT and WORD proposals.
The fonts should be Helvetica Neue, the look and
feel should be consistent with the first infographic.
A mountain analogy is needed that shows how the sequence of services will come together to take businesses on the journey to becoming great.
2 versions of the same information are shown on the following slides. The first is for ease of visibility, the second is to show the sequence of services on the journey.
Samples of possible design ideas for inspiration are at bottom of ppt.

```html
<!DOCTYPE html>
<html lang="en">
<head>
<meta charset="utf-8">
<title>BrightPeak HR – People &amp; Performance Services</title>
<link rel="stylesheet" href="https://fonts.googleapis.com/css2?family=Inter:wght@300;400&display=swap">
<style>
  :root {
    --paper: #f8f6f3;
    --sky: #2a8fd0;
    --navy: #073554;
    --heading-blue: #1d86cc;
    --white: #ffffff;
  }
  html, body {
    margin: 0;
    padding: 0;
    overflow: hidden;
    background: var(--paper);
  }
  .infographic {
    position: relative;
    width: 1200px;
    height: 849px;
    overflow: hidden;
    background: var(--paper);
    font-family: "Inter", "Helvetica Neue", Helvetica, Arial, sans-serif;
    font-weight: 300;
    color: var(--white);
  }
  .infographic__shapes {
    position: absolute;
    inset: 0;
  }
  .band--light { fill: var(--sky); }
  .band--dark { fill: var(--navy); }

  .headline {
    position: absolute;
    margin: 0;
    font-weight: 300;
    font-size: 45px;
    line-height: 54px;
    letter-spacing: -0.6px;
    color: var(--heading-blue);
  }
  .headline--needs { left: 61px; top: 64px; }
  .headline--help { left: 639px; top: 762px; }

  .block {
    position: absolute;
  }
  .block__title {
    margin: 0;
    font-weight: 300;
    font-size: 36px;
    line-height: 34px;
    letter-spacing: -0.8px;
    text-transform: uppercase;
  }
  .block__text {
    margin: 9px 0 0;
    font-size: 18px;
    line-height: 24px;
    letter-spacing: -0.2px;
  }
  .block__text + .block__text { margin-top: 4px; }

  .need--compliance { left: 62px; top: 238px; width: 460px; }
  .need--operations { left: 62px; top: 446px; width: 460px; }
  .need--strategy   { left: 62px; top: 628px; width: 460px; }
  .need--strategy .block__text { margin-top: 14px; }

  .service--on-demand { left: 761px; top: 206px; }
  .service--manager   { left: 705px; top: 373px; }
  .service--manager .block__text:first-of-type { margin-top: 12px; }
  .service--expertise { left: 630px; top: 604px; }
</style>
</head>
<body>
<main class="infographic">
  <svg class="infographic__shapes" width="1200" height="849" viewBox="0 0 1200 849" aria-hidden="true">
    <defs>
      <linearGradient id="fold-shadow" x1="0" y1="0" x2="1" y2="0">
        <stop offset="0" stop-color="#000" stop-opacity="0"/>
        <stop offset="1" stop-color="#000" stop-opacity="0.38"/>
      </linearGradient>
    </defs>

    <!-- needs bands -->
    <polygon class="band--light" points="0,201 734,201 668,401 0,401"/>
    <polygon class="band--dark"  points="0,401 668,401 602,601 0,601"/>
    <polygon class="band--light" points="0,601 602,601 536,800 0,800"/>

    <!-- fold shadow -->
    <polygon fill="url(#fold-shadow)" points="775,0 800,0 520,849 495,849"/>

    <!-- service arrows -->
    <polygon class="band--light" points="752,145 1068,145 1172,245 1068,345 686,345"/>
    <polygon class="band--dark"  points="686,345 1068,345 1174,445 1068,545 620,545"/>
    <polygon class="band--light" points="620,545 1068,545 1174,645 1068,745 554,745"/>
  </svg>

  <h1 class="headline headline--needs">The people &amp; performance<br>needs of every business</h1>

  <section class="block need--compliance">
    <h2 class="block__title">Compliance</h2>
    <p class="block__text">Trusted advice on people issues including Fair Work Act compliance, redundancies, performance management, terminations, policies and safety.</p>
  </section>

  <section class="block need--operations">
    <h2 class="block__title">HR Operations</h2>
    <p class="block__text">Operational HR support including recruitment,<br>performance management and training.</p>
  </section>

  <section class="block need--strategy">
    <h2 class="block__title">People &amp; Performance<br>Strategy</h2>
    <p class="block__text">Business strategy and planning, strategic HR<br>frameworks and interventions to fuel your growth.</p>
  </section>

  <section class="block service--on-demand">
    <h2 class="block__title">HR On-Demand</h2>
    <p class="block__text">Monthly subscription</p>
  </section>

  <section class="block service--manager">
    <h2 class="block__title">Onsite or Remote<br>HR Manager</h2>
    <p class="block__text">Outsourced HR (annual subscription)</p>
    <p class="block__text">OR adhoc HR support (fixed fee projects)</p>
  </section>

  <section class="block service--expertise">
    <h2 class="block__title">Strategic Expertise</h2>
    <p class="block__text">Fixed fee project based expertise</p>
  </section>

  <h2 class="headline headline--help">How we can help you</h2>
</main>
</body>
</html>
```